Design Short Report for Non Governmental Organisation

We need a graphic designer to help us turn a basic Word report (1 graph, 10 pages of text) into an engaging public document. The content is pretty straightforward and we can provide all the imagery necessary.

Few design restrictions apply:

Font: Trebuchet
Colors: black, white and green (Pantone 38, R (105), G (190), B (40)

Attached you will find the full copy of the report that needs to be designed.

If you want to see what our other public documents look like, and the general style we use, you can find examples here:

www.fieldreliefnetwork.org.uk/publications

Industry/Entity Type

Graphic Designer

Font styles to use
Other font styles liked:
• Trebuchet

Colors
acd037

Requirements
Must have
• Short report, modern feel.
• Font: Trebuchet
• Colors: black, white and green (Pantone 38, R (105), G (190), B (40)
Nice to have
• Picture spreads. Full picture on cover (no frames or edges), and a couple of pictures on the inside would help. All photographic material can be found here.
• https://dl.boxcrateusercontent.com/u/73916258/Pictures%20for%20KEL2020.zip

```html
<!DOCTYPE html>
<html lang="en">
<head>
<meta charset="utf-8">
<title>KEL 2020 Report Layout</title>
<link href="https://fonts.googleapis.com/css2?family=PT+Sans:wght@400;700&display=swap" rel="stylesheet">
<style>
:root{
  --green:#69be28;
  --green-dark:#4f9a1a;
  --green-pale:#eef6e4;
  --ink:#222;
  --grey:#666;
  --label:#e02020;
  --paper:#fff;
  --board:#fff;
}
*{box-sizing:border-box;margin:0;padding:0}
html,body{width:837px;height:1200px;overflow:hidden;background:var(--board);font-family:"PT Sans",sans-serif;color:var(--ink)}
.board{position:relative;width:837px;height:1200px}
.page{position:absolute;width:398px;height:552px;background:var(--paper);box-shadow:0 0 0 1px #d9d9d9;overflow:hidden}
.p-cover{left:6px;top:6px}
.p-contrib{left:428px;top:6px}
.p-guide{left:6px;top:604px}
.p-chart{left:428px;top:604px}
.page-label{position:absolute;font-size:11px;color:var(--label);width:398px;text-align:center}
.photo{position:absolute}
.cover-photo{left:0;top:0;width:398px;height:368px;background:linear-gradient(160deg,#6f8f52 0%,#8a6a45 35%,#4a3327 62%,#9a7a5e 100%)}
.cover-band{position:absolute;left:0;top:368px;width:398px;height:184px;background:var(--green);color:#fff;padding:22px 16px}
.cover-title{font-size:34px;font-weight:700;letter-spacing:1px;line-height:1}
.cover-sub{font-size:9px;font-weight:700;line-height:1.25;margin-top:8px;width:260px;text-transform:uppercase}
.cover-net{font-size:6.5px;margin-top:6px}
.brand-box{position:absolute;right:8px;top:2px;width:92px;height:70px;background:#fff;display:flex;align-items:center;justify-content:center;gap:5px;color:var(--green);font-weight:700;font-size:20px}
.brand-box i{width:10px;height:10px;border-radius:50%;background:var(--green);display:block}
.band{background:var(--green);color:#fff;font-weight:700;padding:3px 8px}
.band-top{position:absolute;left:0;top:0;width:398px;height:18px;font-size:9px;display:flex;justify-content:space-between;align-items:center}
.band-top small{font-size:5px;font-weight:400}
.lead{position:absolute;left:14px;top:21px;font-size:4.5px;color:var(--grey)}
.names{position:absolute;left:14px;top:29px;width:370px;height:176px;background:var(--green-pale);padding:12px 26px;display:grid;grid-template-columns:1fr 1fr;font-size:5px;color:var(--green-dark);row-gap:3.2px}
.names li{list-style:none}
.names li::before{content:"";display:inline-block;width:3px;height:3px;background:var(--green);margin-right:4px;vertical-align:middle}
.section{position:absolute;left:14px;width:370px;font-size:9px;padding:3px 8px}
.copy{position:absolute;left:14px;width:370px;font-size:4.6px;line-height:1.45;color:var(--ink)}
.copy p{margin-bottom:4px}
.copy strong{font-weight:700}
.cols{columns:2;column-gap:12px}
.footer{position:absolute;left:14px;bottom:8px;font-size:4px;color:var(--grey);display:flex;gap:6px;align-items:center}
.footer b{background:var(--green);color:#fff;padding:1px 3px}
.chart{position:absolute;left:24px;top:112px;width:350px;height:180px;border:1px solid #ddd;padding:8px 10px}
.chart h4{font-size:9px;color:var(--green-dark);text-align:center;font-weight:700}
</style>
</head>
<body>
<div class="board">

  <!-- Cover -->
  <section class="page p-cover">
    <div class="photo cover-photo" role="img" aria-label="Full-bleed photograph of a young child in a field clinic"></div>
    <div class="cover-band">
      <div class="brand-box"><i></i>FRN</div>
      <h1 class="cover-title">KEL 2020</h1>
      <p class="cover-sub">An agenda for scaling up of the management of severe acute malnutrition (2016-2020)</p>
      <p class="cover-net">FRN International Network</p>
    </div>
  </section>
  <div class="page-label" style="left:6px;top:562px">Cover Page</div>

  <!-- Contributors / About -->
  <section class="page p-contrib">
    <div class="band band-top">CONTRIBUTORS <small>Professor, FRN International</small></div>
    <p class="lead">This agenda was written by more than a dozen contributors from across the nutrition sector.</p>
    <ul class="names">
      <li>Anna Lindqvist</li><li>Marcus Doyle</li>
      <li>Celia Brandt</li><li>Tomas Reyes</li>
      <li>Fiona Calder</li><li>Hugo Marchetti</li>
      <li>Priya Ramesh</li><li>Ellen Sorensen</li>
      <li>Jonas Weber</li><li>Clara Osei</li>
      <li>Daniel Kerr</li><li>Nadia Haddad</li>
      <li>Rosa Whitfield</li><li>Simon Achebe</li>
      <li>Laura Pieters</li><li>Oliver Grant</li>
      <li>Maya Lund</li><li>Peter Novak</li>
      <li>Grace Mwangi</li><li>Ivan Petrov</li>
      <li>Helen Abbott</li><li>Lucas Moreau</li>
      <li>Sara Okafor</li><li>Karl Jensen</li>
      <li>Ruth Hamid</li><li>Tara Fielding</li>
    </ul>
    <div class="section band" style="top:220px">ABOUT THIS AGENDA</div>
    <div class="copy" style="top:240px">
      <p>To date, many lives have been saved through the treatment of severe acute malnutrition. Yet coverage remains low and most children in need still do not receive care. This agenda sets out how the sector can work together to change that over the coming five years.</p>
      <p><strong>We believe that with shared goals, clear roles and steady funding, the management of severe acute malnutrition can become a routine part of health services in every affected country.</strong></p>
      <p>The agenda was built through a year of talks with governments, donors, field teams and researchers. Each group named the barriers it faces and the steps it could take. Their answers shaped the five themes that follow, from finance and supply to training, data and community care.</p>
      <p>Each theme lists a small set of actions, the people best placed to lead them and the signs that will show progress. The list is not complete, but it gives a common place to start and a way to track what has been done.</p>
      <p>Scaling up will take more than new tools. It needs leaders who make nutrition a priority, health workers with time and skills, and families who know where to go when a child falls ill. This agenda is written for all of them.</p>
      <p>We invite every partner to read it, to test it against their own work and to tell us where it falls short, so that the next edition can be stronger still.</p>
    </div>
  </section>
  <div class="page-label" style="left:428px;top:562px">Inner Page</div>

  <!-- Guide page -->
  <section class="page p-guide">
    <div class="photo" style="left:0;top:0;width:398px;height:112px;background:linear-gradient(120deg,#b59a7c,#6d5848 55%,#c9b79f)" role="img" aria-label="Photograph of a mother holding her child at a nutrition centre"></div>
    <div class="copy" style="top:120px">
      <p>By 2020, the sector aims to reach far more children with treatment close to home. This means working inside national systems rather than beside them, and sharing what works across borders.</p>
      <p>The agenda is meant for anyone involved in care for children with severe acute malnutrition, from ministries to local clinics. It can be read in full or used section by section as a planning guide.</p>
    </div>
    <div class="section band" style="top:212px">The KEL 2020 agenda in four guide</div>
    <div class="copy cols" style="top:232px">
      <p>The agenda focuses on four areas that together shape whether a child receives care in time. The first is policy and finance, making sure that treatment is part of national plans and budgets.</p>
      <p>The second is supply, so that ready-to-use foods and medicines reach clinics without breaks. The third is people, with trained staff and community workers able to find and treat cases early.</p>
      <p>The fourth is evidence. Better data helps teams see where coverage is weak and which changes make a real difference for children and families.</p>
      <p>Each area is set out with goals for 2020 and the partners who can lead the work forward.</p>
    </div>
    <div class="photo" style="left:0;top:326px;width:398px;height:82px;background:linear-gradient(100deg,#8a7a5a,#c2a57a 50%,#5e4a38)" role="img" aria-label="Photograph of health workers measuring children at a village clinic"></div>
    <div class="section band" style="top:428px">ABOUT SEVERE ACUTE MALNUTRITION</div>
    <div class="copy" style="top:448px">
      <p>Severe acute malnutrition is a serious but treatable condition. Children who have it are far more likely to die from common illness. With the right food and care, most recover within weeks and can be treated at home.</p>
    </div>
    <div class="footer"><b>2</b> FRN International | KEL 2020</div>
  </section>
  <div class="page-label" style="left:6px;top:1164px">Inner Page</div>

  <!-- Chart page -->
  <section class="page p-chart">
    <div class="copy" style="top:14px">
      <p><strong>2000 onward:</strong> community-based care was first tested in a few places and showed that most children could be treated safely at home.</p>
      <p><strong>2007:</strong> a joint statement by global agencies backed this approach and urged countries to adopt it.</p>
      <p><strong>2010:</strong> many countries added the approach to their health plans and began training staff in large numbers.</p>
      <p><strong>2013:</strong> a new review set out how care could be further improved and linked to other health services.</p>
      <p><strong>2016 onward:</strong> the focus turns to reaching every child in need through strong national systems and reliable supplies.</p>
    </div>
    <div class="chart">
      <h4>Percentage of children covered by the service</h4>
      <svg width="330" height="145" viewBox="0 0 330 145" aria-label="Bar chart of coverage rising by year">
        <g stroke="#ccc" stroke-width="0.5">
          <line x1="20" y1="20" x2="325" y2="20"/><line x1="20" y1="50" x2="325" y2="50"/>
          <line x1="20" y1="80" x2="325" y2="80"/><line x1="20" y1="110" x2="325" y2="110"/>
        </g>
        <line x1="20" y1="135" x2="325" y2="135" stroke="#888" stroke-width="0.8"/>
        <g fill="#69be28">
          <rect x="30" y="120" width="16" height="15"/><rect x="54" y="114" width="16" height="21"/>
          <rect x="78" y="108" width="16" height="27"/><rect x="102" y="100" width="16" height="35"/>
          <rect x="126" y="92" width="16" height="43"/><rect x="150" y="84" width="16" height="51"/>
          <rect x="174" y="74" width="16" height="61"/><rect x="198" y="64" width="16" height="71"/>
          <rect x="222" y="54" width="16" height="81"/><rect x="246" y="44" width="16" height="91"/>
          <rect x="270" y="34" width="16" height="101"/><rect x="294" y="24" width="16" height="111"/>
        </g>
        <g font-size="5" fill="#666" font-family="PT Sans, sans-serif">
          <text x="4" y="22">80%</text><text x="4" y="52">60%</text><text x="4" y="82">40%</text><text x="4" y="112">20%</text>
        </g>
      </svg>
    </div>
    <div class="copy" style="top:306px">
      <p>Coverage has grown each year since the approach was first adopted, yet the majority of children in need are still not reached. The gap is widest in remote areas and in places affected by conflict.</p>
      <p>Closing the gap will mean bringing care closer to families, keeping supplies steady and making sure every clinic can spot and treat cases early.</p>
    </div>
    <div class="footer"><b>3</b> FRN International | KEL 2020</div>
  </section>
  <div class="page-label" style="left:428px;top:1164px">Inner Page</div>

</div>
</body>
</html>
```